Ecommerce Website For Printing Company

Zoravquill.com are a print, design and signage company who sell flyers, business cards, posters, brochures and more to customers in the UK.

Our website is outdated and requires a new design using current web styling and mobile functionality.

We require the following pages to be designed;
- Home Page
- Price Page
- Portfolio Page
- Blog
- Content Page

Our competitors in the printing industry are www.brenticade.com, www.hallowmarsh.co.uk, quorelvane.co.uk, www.tambridok.co.uk

We require the website to give a professional image as well as be easy for customers to navigate, understand and find prices.

Target Market(s)

Businesses

Industry/Entity Type

Printing

Number of Pages Required

4 page

Font styles to use
Sans Serif

Colors
33a6d7

Requirements
Must have
• Popular products, latest news/blog, sales from portfolio, newsletter sign up, footer

```html
<!DOCTYPE html>
<html lang="en">
<head>
<meta charset="utf-8">
<title>Zoravquill.com – Print, Design &amp; Signage</title>
<link href="https://fonts.googleapis.com/css2?family=Open+Sans:wght@400;600;700;800&display=swap" rel="stylesheet">
<style>
:root{
  --brand:#33a6d7;
  --brand-dark:#1f86b4;
  --ink:#333;
  --muted:#888;
  --dark:#1e2226;
  --panel:#f1f1f1;
  --accent:#f5a623;
  --white:#fff;
}
*{box-sizing:border-box;margin:0;padding:0}
html,body{width:703px;height:1200px;overflow:hidden}
body{font-family:"Open Sans",Arial,sans-serif;color:var(--ink);background:var(--white);font-size:6px;line-height:1.35}
a{color:inherit;text-decoration:none}

.topbar{height:14px;background:var(--dark);color:#cfd6db;display:flex;align-items:center;justify-content:space-between;padding:0 40px;font-size:5px}
.topbar .quick{display:flex;gap:10px}

.site-header{height:56px;background:var(--brand);display:flex;align-items:center;justify-content:space-between;padding:0 40px}
.logo{display:flex;align-items:center;gap:5px;background:var(--white);padding:6px 10px;border-radius:3px}
.logo-mark{width:12px;height:12px;background:var(--brand);border-radius:50%}
.logo-name{font-size:15px;font-weight:800;color:var(--brand)}
.main-nav{display:flex;gap:13px;color:var(--white);font-size:6.5px;font-weight:700;text-transform:uppercase}

.hero{position:relative;height:192px;background:linear-gradient(180deg,#5a3a25,#7a5034 55%,#4a2e1d)}
.hero-copy{position:absolute;left:88px;top:42px;color:var(--white)}
.hero-copy h1{font-size:25px;font-weight:800;line-height:1.05}
.hero-copy p{font-size:9px;font-weight:600;margin-top:4px;width:190px;line-height:1.25}
.btn-order{display:inline-block;margin-top:12px;background:var(--accent);color:var(--white);font-weight:800;font-size:7px;padding:6px 12px;border-radius:2px}
.price-badge{position:absolute;left:278px;top:78px;width:56px;height:56px;border-radius:50%;background:var(--brand);color:var(--white);display:flex;flex-direction:column;align-items:center;justify-content:center;border:2px solid var(--white)}
.price-badge small{font-size:8px;font-weight:600;line-height:1}
.price-badge strong{font-size:18px;font-weight:800;line-height:1}
.hero-visual{position:absolute;left:350px;top:12px;width:290px;height:168px;background:linear-gradient(135deg,#b9d9e8,#e9c98a 50%,#3b6d8c);transform:rotate(-3deg);border-radius:2px;opacity:.85}
.hero-dots{position:absolute;left:50%;bottom:8px;transform:translateX(-50%);display:flex;gap:4px}
.hero-dots span{width:5px;height:5px;border-radius:50%;background:rgba(255,255,255,.5)}
.hero-dots span:first-child{background:var(--white)}

.popular{height:218px;background:var(--panel);padding:14px 40px}
.popular-panel{background:var(--white);height:190px;padding:10px 12px;position:relative}
.section-label{font-size:8px;font-weight:700;text-transform:uppercase;border-bottom:1px solid #e3e3e3;padding-bottom:6px}
.product-row{display:flex;gap:12px;margin:12px 18px 0}
.product-card{flex:1;border:1px solid #e6e6e6;padding:5px}
.product-thumb{height:72px}
.product-card .name{display:flex;justify-content:space-between;margin-top:5px;font-size:7px;font-weight:700}
.product-card .name span:first-child{color:var(--brand)}
.product-card p{color:var(--muted);font-size:5px;margin-top:3px}
.slide-arrow{position:absolute;top:90px;font-size:12px;color:#aaa}
.slide-arrow.prev{left:10px}.slide-arrow.next{right:10px}

.portfolio{height:220px;padding:16px 40px 0;text-align:center}
.portfolio h2{font-size:15px;font-weight:400;color:#555}
.portfolio h2 strong{font-weight:800;color:var(--ink)}
.filter-bar{display:flex;justify-content:space-between;font-size:5.5px;color:var(--muted);margin:8px 40px 8px;text-transform:uppercase}
.filter-bar .active{color:var(--brand);font-weight:700}
.work-grid{display:grid;grid-template-columns:repeat(5,80px);gap:12px 14px;justify-content:center}
.work-item{height:72px;border:1px solid #ddd}

.testimonial{position:relative;height:190px;background:linear-gradient(90deg,#2b3035,#3d4650 50%,#2a2f34);color:var(--white);text-align:center;padding-top:22px}
.avatar{width:40px;height:40px;border-radius:50%;background:#c8a590;margin:0 auto;border:2px solid var(--white)}
.testimonial blockquote{font-size:7px;width:470px;margin:14px auto 0;font-style:italic;line-height:1.55}
.testimonial .cite{display:block;margin-top:8px;color:var(--brand);font-weight:700;font-size:6.5px}

.news{height:225px;display:flex;gap:30px;padding:18px 40px 0}
.blog{flex:1.3}
.news h2{font-size:14px;font-weight:700;margin-bottom:10px}
.post{display:flex;gap:8px;margin-bottom:14px}
.post-thumb{width:56px;height:44px;flex:none}
.post h3{font-size:7px;font-weight:700;color:var(--brand)}
.post .date{color:var(--muted);font-size:5px}
.post p{font-size:5.5px;color:#666;margin-top:2px}
.post .more{font-size:5.5px;color:var(--brand);font-weight:700}
.feed{flex:1}
.feed h3{font-size:8px;font-weight:700;display:flex;align-items:center;gap:5px;margin:6px 0 10px}
.feed h3 i{width:9px;height:9px;border-radius:50%;background:var(--brand);display:inline-block}
.feed-item{font-size:5.5px;color:#555;margin-bottom:9px;border-bottom:1px solid #eee;padding-bottom:6px}
.feed-item b{color:var(--brand)}

.newsletter{height:28px;background:var(--dark);display:flex;align-items:center;justify-content:center;gap:14px;color:var(--white)}
.newsletter strong{font-size:8px}
.newsletter .field{width:140px;height:14px;background:var(--white);color:#999;font-size:5.5px;padding:3px 5px}
.newsletter .btn{background:var(--brand);font-weight:700;font-size:6px;padding:3px 10px}

.site-footer{height:44px;background:var(--brand);color:var(--white);display:flex;gap:28px;padding:5px 40px;font-size:4.8px}
.site-footer h4{font-size:6px;font-weight:700;margin-bottom:2px}
.site-footer ul{list-style:none;line-height:1.3}
.pay{display:flex;gap:3px;margin-top:2px}
.pay span{width:16px;height:10px;background:var(--white);opacity:.85;border-radius:1px}
.social{display:flex;gap:3px;margin-top:3px}
.social span{width:8px;height:8px;border-radius:50%;background:var(--white)}

.copyright{height:13px;background:var(--brand-dark);color:#e1f2fa;font-size:4.8px;display:flex;align-items:center;justify-content:space-between;padding:0 40px}
</style>
</head>
<body>

<div class="topbar">
  <span>NEED HELP? CALL US ON 01632 960 418</span>
  <div class="quick"><span>Login</span><span>My Account</span><span>Basket (0)</span><span>Upload Artwork</span></div>
</div>

<header class="site-header">
  <a class="logo" href="#"><span class="logo-mark"></span><span class="logo-name">Zoravquill</span></a>
  <nav class="main-nav">
    <a href="#">Home</a><a href="#">About</a><a href="#">Printing</a><a href="#">Graphic Design</a><a href="#">Website Design</a><a href="#">Artwork Guide</a><a href="#">Upload</a>
  </nav>
</header>

<section class="hero">
  <div class="hero-visual" role="img" aria-label="Stack of printed A5 flyers fanned out on a wooden desk"></div>
  <div class="hero-copy">
    <h1>5000 A5 Flyers</h1>
    <p>Printed on 130gsm gloss, full colour double sided design...</p>
    <a class="btn-order" href="#">ORDER NOW</a>
  </div>
  <div class="price-badge"><small>only</small><strong>£96</strong></div>
  <div class="hero-dots"><span></span><span></span><span></span></div>
</section>

<section class="popular">
  <div class="popular-panel">
    <div class="section-label">Popular Products</div>
    <span class="slide-arrow prev">‹</span><span class="slide-arrow next">›</span>
    <div class="product-row">
      <article class="product-card">
        <div class="product-thumb" role="img" aria-label="Business cards product photo" style="background:linear-gradient(135deg,#e8eef2,#9fb6c4)"></div>
        <div class="name"><span>Business Cards</span><span>£19</span></div>
        <p>Premium 400gsm cards with a choice of matt or gloss finish, printed full colour on both sides.</p>
      </article>
      <article class="product-card">
        <div class="product-thumb" role="img" aria-label="A4 letterheads product photo" style="background:linear-gradient(135deg,#f3efe6,#b8a98d)"></div>
        <div class="name"><span>A4 Letterheads</span><span>£45</span></div>
        <p>Crisp 120gsm bond letterheads ready for office printers, ideal for invoices and letters.</p>
      </article>
      <article class="product-card">
        <div class="product-thumb" role="img" aria-label="A5 flyers product photo" style="background:linear-gradient(135deg,#2d3a44,#c97a45)"></div>
        <div class="name"><span>A5 Flyers</span><span>£25</span></div>
        <p>Eye catching flyers on 130gsm gloss, perfect for promotions, events and local mailings.</p>
      </article>
      <article class="product-card">
        <div class="product-thumb" role="img" aria-label="A4 posters product photo" style="background:linear-gradient(135deg,#d9e4ea,#5c7d8f)"></div>
        <div class="name"><span>A4 Posters</span><span>£31</span></div>
        <p>Vivid full colour posters on silk paper, great for shop windows and notice boards.</p>
      </article>
    </div>
  </div>
</section>

<section class="portfolio">
  <h2>Take a Look at <strong>Our Work</strong></h2>
  <div class="filter-bar"><span>Filter by type</span><span><span class="active">All</span> / Web Design / Graphic Design</span></div>
  <div class="work-grid">
    <div class="work-item" role="img" aria-label="Printed brochure sample" style="background:linear-gradient(135deg,#e9dfc9,#8c6d48)"></div>
    <div class="work-item" role="img" aria-label="Event flyer sample" style="background:linear-gradient(135deg,#f0f0f0,#c3372f)"></div>
    <div class="work-item" role="img" aria-label="Shop signage sample" style="background:linear-gradient(135deg,#f7d34a,#e07a1f)"></div>
    <div class="work-item" role="img" aria-label="Leaflet design sample" style="background:linear-gradient(135deg,#2e4f8a,#d94a6b)"></div>
    <div class="work-item" role="img" aria-label="Stationery set sample" style="background:linear-gradient(135deg,#f4f4f4,#c8a45a)"></div>
    <div class="work-item" role="img" aria-label="Vehicle graphics sample" style="background:linear-gradient(135deg,#1d6fb3,#7cc4e8)"></div>
    <div class="work-item" role="img" aria-label="Restaurant menu sample" style="background:linear-gradient(135deg,#d94a32,#f2c14e)"></div>
    <div class="work-item" role="img" aria-label="Booklet cover sample" style="background:linear-gradient(135deg,#3a8f4a,#b7dca0)"></div>
    <div class="work-item" role="img" aria-label="Banner design sample" style="background:linear-gradient(135deg,#e6e1d6,#4f6b7a)"></div>
    <div class="work-item" role="img" aria-label="Display board sample" style="background:linear-gradient(135deg,#d7c7b0,#7b5a3e)"></div>
  </div>
</section>

<section class="testimonial" role="img" aria-label="Darkened office workspace background photo">
  <div class="avatar" role="img" aria-label="Customer portrait"></div>
  <blockquote>“We were delighted with our new flyers and the service from start to finish. The team helped us tidy our artwork, answered every question quickly and the printed job arrived a day early. We will certainly be ordering again for our next campaign.”</blockquote>
  <span class="cite">Read more customer reviews</span>
</section>

<section class="news">
  <div class="blog">
    <h2>Our Blog</h2>
    <article class="post">
      <div class="post-thumb" role="img" aria-label="Blog post photo of printed leaflets" style="background:linear-gradient(135deg,#c3d6e2,#5d7e93)"></div>
      <div>
        <h3>Choosing the right paper</h3>
        <span class="date">Posted 12 March</span>
        <p>A quick guide to paper weights and finishes so your next print job looks and feels exactly right for your brand.</p>
        <span class="more">Read more</span>
      </div>
    </article>
    <article class="post">
      <div class="post-thumb" role="img" aria-label="Blog post photo of a design studio" style="background:linear-gradient(135deg,#e4d5c2,#9b7454)"></div>
      <div>
        <h3>Our New Studio Printer</h3>
        <span class="date">Posted 28 February</span>
        <p>We have added a new large format printer to the studio, meaning faster turnaround on posters, banners and signs.</p>
        <span class="more">Read more</span>
      </div>
    </article>
  </div>
  <div class="feed">
    <h3><i></i>Our Chirpline feed</h3>
    <div class="feed-item"><b>@zoravquill</b> Spring offer now live: 20% off all business cards this week only. <b>2 hours ago</b></div>
    <div class="feed-item"><b>@zoravquill</b> Fresh batch of menus heading out to a local café today. <b>1 day ago</b></div>
    <div class="feed-item"><b>@zoravquill</b> Need artwork help? Our design team can check files for free. <b>3 days ago</b></div>
    <div class="feed-item" style="border:0">Follow us for news</div>
  </div>
</section>

<section class="newsletter">
  <strong>Sign up to our newsletter for updates on our special deals</strong>
  <span class="field">Enter your email address</span>
  <span class="btn">SIGN UP</span>
</section>

<footer class="site-footer">
  <div><h4>Links</h4><ul><li>Printing</li><li>Graphic Design</li><li>Web Design</li></ul></div>
  <div><h4>Product Range</h4><ul><li>Business Cards</li><li>Flyers &amp; Leaflets</li><li>Posters</li></ul></div>
  <div><h4>Account</h4><ul><li>My Account</li><li>Order History</li><li>Upload</li></ul></div>
  <div><h4>We Accept</h4><div class="pay"><span></span><span></span><span></span><span></span></div></div>
  <div><h4>Get In Touch</h4><ul><li>14 Fenwick Row, Harlton, HT4 7QD</li><li>Phone: 01632 960 418</li><li>hello@zoravquill.com</li></ul><div class="social"><span></span><span></span><span></span></div></div>
</footer>

<div class="copyright"><span>© Zoravquill.com. All rights reserved.</span><span>Terms &amp; Conditions | Privacy Policy</span></div>

</body>
</html>
```